QuillHarbor New Website

QuillHarbor is a digital marketing agency. Our clients are all limousine companies. We need a responsive website designed to highlight our services and products. Our competition is http://www.velmorastudiohub.com/ and we need a site of similar design and layout without being too similar. Our old website www.quillharbor.com, is very outdated and the logo and graphics have changed. We will adjust the content to work with the new design. The new logo is attached.

Industry/Entity Type

Digital

Coding

Coded - Design and coding required

```html
<!DOCTYPE html>
<html lang="en">
<head>
<meta charset="utf-8">
<title>QuillHarbor — Limousine Marketing Partners</title>
<link rel="stylesheet" href="https://fonts.googleapis.com/css2?family=Raleway:wght@300;400;500;600;700;800&family=Roboto:ital,wght@0,300;0,400;0,500;1,400;1,500;1,700&display=swap">
<style>
:root{
  --gold:#b8a44e;
  --gold-light:#c6b25a;
  --navy:#1a4a63;
  --ink:#333333;
  --muted:#777777;
  --soft:#f6f6f6;
  --line:#dddddd;
  --footer:#2b2b2b;
  --white:#ffffff;
}
*{box-sizing:border-box;margin:0;padding:0}
html,body{width:1200px;height:2378px;overflow:hidden;background:var(--white)}
body{position:relative;font-family:"Roboto",Arial,sans-serif;color:var(--ink)}
.abs{position:absolute}

/* header */
.site-header{position:absolute;left:0;top:0;width:1200px;height:130px;background:var(--white)}
.brand{position:absolute;left:141px;top:30px}
.brand-name{font-family:"Raleway",sans-serif;font-weight:400;font-size:46px;color:var(--navy);letter-spacing:-.5px;line-height:1}
.brand-note{font-family:"Roboto",sans-serif;font-weight:400;font-size:12px;color:#888;margin:9px 0 0 3px}
.topbar{position:absolute;right:144px;top:0;height:34px;display:flex;border-left:1px solid #eee}
.topbar span{display:flex;align-items:center;gap:8px;padding:0 12px;font-size:11px;color:#666;border-right:1px solid #eee}
.main-nav{position:absolute;right:144px;top:67px;display:flex;gap:17px;font-family:"Raleway",sans-serif;font-size:13.5px;font-weight:500;color:#333}

/* hero */
.hero{position:absolute;left:0;top:130px;width:1200px;height:453px}
.hero-photo{position:absolute;inset:0;background:linear-gradient(120deg,#3e4650 0%,#5a6068 35%,#4a4e55 60%,#6b6f75 100%)}
.hero-shade{position:absolute;inset:0;background:rgba(20,20,25,.35)}
.hero-line{position:absolute;left:0;width:1200px;text-align:center;font-family:"Raleway",sans-serif;font-weight:300;font-size:38px;color:var(--white);letter-spacing:.5px}
.hero-title{position:absolute;left:0;top:218px;width:1200px;text-align:center;font-family:"Raleway",sans-serif;font-weight:800;font-size:38px;color:var(--white);letter-spacing:.5px}
.btn{position:absolute;top:333px;height:35px;border-radius:3px;font-family:"Raleway",sans-serif;font-weight:500;font-size:13px;display:flex;align-items:center;justify-content:center;color:#222}
.btn-start{left:477px;width:121px;background:var(--gold-light)}
.btn-learn{left:605px;width:122px;background:#bdbdbd}

/* services */
.service{position:absolute;top:640px;width:200px;text-align:center}
.service-icon{width:106px;height:106px;margin:0 auto;border-radius:50%;background:#f5f5f5;border:1px solid #e6e6e6;display:flex;align-items:center;justify-content:center}
.service-icon.active{background:var(--navy);border-color:var(--navy)}
.service-title{margin-top:27px;font-family:"Raleway",sans-serif;font-weight:500;font-size:13px;letter-spacing:.5px;color:#222}
.service-text{margin-top:10px;font-size:11px;line-height:13px;color:#777}

/* statement */
.statement{position:absolute;left:0;top:905px;width:1200px;height:319px;background:linear-gradient(180deg,#151515,#0c0c0c)}
.statement p{position:absolute;left:145px;top:63px;width:910px;text-align:center;font-size:34px;line-height:49px;color:var(--white);font-weight:400}
.statement em{color:var(--gold);font-weight:700}
.statement strong{font-style:italic;font-weight:700}

/* team */
.section-title{position:absolute;left:0;width:1200px;text-align:center;font-family:"Raleway",sans-serif;font-weight:400;font-size:34px;color:#333}
.title-rule{position:absolute;height:1px;background:#999}
.member{position:absolute;top:1373px;width:237px}
.member-photo{height:196px}
.member-name{margin-top:17px;text-align:center;font-family:"Raleway",sans-serif;font-size:15px;font-weight:500;color:#222}
.member-role{margin-top:5px;text-align:center;font-size:11px;font-style:italic;color:#777}

/* about */
.about{position:absolute;left:0;top:1700px;width:1200px;height:414px;background:var(--soft)}
.about-photo{position:absolute;left:143px;top:31px;width:407px;height:330px;background:linear-gradient(160deg,#cfd4d8,#9aa2aa 60%,#7d858c)}
.about-heading{position:absolute;left:595px;top:30px;font-family:"Raleway",sans-serif;font-size:34px;color:#333}
.about-rule{position:absolute;left:595px;top:84px;width:66px;height:1px;background:#999}
.about-lead{position:absolute;left:597px;top:117px;width:330px;font-size:15px;line-height:24px;color:#777}
.about-body{position:absolute;left:595px;top:252px;width:450px;font-size:13px;line-height:24px;color:#888}

/* footer */
.site-footer{position:absolute;left:0;top:2114px;width:1200px;height:264px;background:var(--footer);color:var(--white)}
.foot-head{position:absolute;top:40px;font-family:"Raleway",sans-serif;font-weight:700;font-size:18px}
.foot-rule{position:absolute;top:70px;width:40px;height:1px;background:#aaa}
.quick-links{position:absolute;left:167px;top:88px;list-style:none;font-size:11px;line-height:25.5px}
.field{position:absolute;left:384px;width:158px;background:#ddd;border:1px solid #bbb;font-size:8px;font-style:italic;color:#888;padding:5px 6px}
.submit{position:absolute;left:384px;top:222px;width:46px;height:16px;background:#1d2d36;font-size:9px;font-weight:700;display:flex;align-items:center;justify-content:center}
.news{position:absolute;left:637px;width:188px;display:flex;gap:8px}
.news-date{width:36px;height:33px;background:#f1f1e8;border:1px solid #bbb;color:#222;text-align:center;flex:none}
.news-date b{display:block;background:var(--gold);color:var(--white);font-size:8px;font-weight:400;line-height:11px}
.news-date span{font-size:14px;line-height:20px}
.news p{font-size:6px;line-height:8px;color:#eee}
.news-rule{position:absolute;left:637px;width:188px;height:1px;background:#777}
.view-all{position:absolute;left:639px;top:219px;font-size:8px;text-decoration:underline;font-style:italic}
.social{position:absolute;left:887px;top:82px;list-style:none;font-family:Georgia,serif;font-size:13px;line-height:27.5px}
.social li{width:120px;display:flex;justify-content:space-between;align-items:center}
.social i{width:13px;height:13px;display:block}
</style>
</head>
<body>

<header class="site-header">
  <div class="brand">
    <div class="brand-name">QuillHarbor</div>
    <div class="brand-note">Limousine marketing partners</div>
  </div>
  <div class="topbar">
    <span><svg width="9" height="9" viewBox="0 0 10 10"><path d="M2 0.5l2 2-1 1.3c.6 1.3 1.6 2.3 2.9 2.9L7.2 5.7l2 2-1.3 1.8C4.5 9.3.7 5.5.5 2z" fill="#1a4a63"/></svg>855-300-4417</span>
    <span><svg width="10" height="8" viewBox="0 0 10 8"><rect width="10" height="8" fill="#1a4a63"/><path d="M0 0l5 4 5-4" stroke="#fff" fill="none"/></svg>info@quillharbor.com</span>
  </div>
  <nav class="main-nav">
    <span>Integrated Marketing</span><span>Services</span><span>News &amp; Events</span><span>RideKeepers™</span><span>Blog</span><span>Contact Us</span>
  </nav>
</header>

<section class="hero">
  <div class="hero-photo" role="img" aria-label="Photo of business people reviewing charts at a desk with a laptop"></div>
  <div class="hero-shade"></div>
  <div class="hero-line" style="top:86px">WE HAVE A PASSION FOR WHAT WE DO.</div>
  <div class="hero-line" style="top:142px">LET US DO WHAT WE DO BEST.</div>
  <div class="hero-title">QUILLHARBOR</div>
  <div class="btn btn-start">START NOW</div>
  <div class="btn btn-learn">LEARN MORE</div>
</section>

<section class="services">
  <div class="service" style="left:152px">
    <div class="service-icon"><svg width="34" height="26" viewBox="0 0 34 26" fill="none" stroke="#222" stroke-width="2"><polyline points="3,22 11,10 19,17 30,4"/><circle cx="3" cy="22" r="2.5"/><circle cx="11" cy="10" r="2.5"/><circle cx="19" cy="17" r="2.5"/><circle cx="30" cy="4" r="2.5"/></svg></div>
    <div class="service-title">INTERNET MARKETING</div>
    <div class="service-text">Lorem ipsum dolor sit amet,<br>consectetur adipisicing elit,<br>sed do eiusmod.</div>
  </div>
  <div class="service" style="left:384px">
    <div class="service-icon active"><svg width="16" height="28" viewBox="0 0 16 28"><rect x="2" y="1" width="12" height="26" rx="3" fill="#fff"/><circle cx="8" cy="7" r="2.5" fill="#1a4a63"/><circle cx="8" cy="14" r="2.5" fill="#1a4a63"/><circle cx="8" cy="21" r="2.5" fill="#1a4a63"/></svg></div>
    <div class="service-title">DRIVE TRAFFIC</div>
    <div class="service-text">Lorem ipsum dolor sit amet,<br>consectetur adipisicing elit,<br>sed do eiusmod.</div>
  </div>
  <div class="service" style="left:618px">
    <div class="service-icon"><svg width="24" height="28" viewBox="0 0 24 28"><path d="M4 12a8 8 0 0 1 16 0" stroke="#222" stroke-width="2" fill="none"/><rect x="2" y="11" width="4" height="7" fill="#222"/><rect x="18" y="11" width="4" height="7" fill="#222"/><rect x="6" y="9" width="12" height="10" rx="5" fill="#222"/><path d="M2 28c0-6 4-8 10-8s10 2 10 8z" fill="#222"/></svg></div>
    <div class="service-title">ONLINE SUPPORT</div>
    <div class="service-text">Lorem ipsum dolor sit amet,<br>consectetur adipisicing elit,<br>sed do eiusmod.</div>
  </div>
  <div class="service" style="left:849px">
    <div class="service-icon"><svg width="30" height="26" viewBox="0 0 30 26" fill="none" stroke="#222" stroke-width="2"><rect x="1" y="1" width="28" height="18"/><polyline points="5,15 11,9 16,12 24,5"/><line x1="15" y1="19" x2="15" y2="24"/><line x1="9" y1="25" x2="21" y2="25"/></svg></div>
    <div class="service-title">DRIVE SALES</div>
    <div class="service-text">Lorem ipsum dolor sit amet,<br>consectetur adipisicing elit,<br>sed do eiusmod.</div>
  </div>
</section>

<section class="statement" role="img" aria-label="Dark background photo of a financial chart">
  <p><em>QuillHarbor</em> and our clients dare to be different.&nbsp; We create campaigns in which <strong>our clients stand out</strong> from the crowd. We help you rise above the "sea of sameness" by not only raising the stakes, but <em>changing the game</em>.</p>
</section>

<section class="team">
  <div class="section-title" style="top:1266px">OUR TEAM</div>
  <div class="title-rule" style="left:567px;top:1328px;width:66px"></div>

  <div class="member" style="left:127px">
    <div class="member-photo" role="img" aria-label="Portrait of a smiling man in a suit in an office" style="background:linear-gradient(135deg,#9a6a52,#6a6f78 50%,#3c4048)"></div>
    <div class="member-name">OWEN TALBRIDGE</div>
    <div class="member-role">Marketing Expert</div>
  </div>
  <div class="member" style="left:364px">
    <div class="member-photo" style="position:relative;background:linear-gradient(135deg,#b8c2c6,#8a959c)" role="img" aria-label="Portrait of a man in a shirt, with a social links overlay">
      <svg class="abs" style="left:0;top:0" width="237" height="196" viewBox="0 0 237 196"><polygon points="40,0 237,0 237,196 0,196" fill="rgba(30,95,120,.55)"/><g fill="none" stroke="#fff" stroke-width="1.5"><circle cx="68" cy="126" r="12"/><circle cx="106" cy="126" r="12"/><circle cx="144" cy="126" r="12"/></g></svg>
    </div>
    <div class="member-name">DALEN MARSH</div>
    <div class="member-role">Web Developer</div>
  </div>
  <div class="member" style="left:598px">
    <div class="member-photo" role="img" aria-label="Portrait of a smiling woman with curly blond hair" style="background:linear-gradient(135deg,#a7ae9a,#c9b89a 50%,#8e938a)"></div>
    <div class="member-name">IRENE CALLOWAY</div>
    <div class="member-role">Marketing Specialist</div>
  </div>
  <div class="member" style="left:835px">
    <div class="member-photo" role="img" aria-label="Portrait of a smiling young man in a grey t-shirt" style="background:linear-gradient(135deg,#f0f0f0,#d8d0c8 50%,#b0b0b0)"></div>
    <div class="member-name">TOBIN REYES</div>
    <div class="member-role">IT Expert</div>
  </div>
</section>

<section class="about">
  <div class="about-photo" role="img" aria-label="Photo of business people meeting around a white table"></div>
  <div class="about-heading">ABOUT US</div>
  <div class="about-rule"></div>
  <p class="about-lead">Lorem ipsum dolor sit amet, consectetur adipi sicing elit, sed do eiusmod tempor inci didunt ut labore et dolore magnaaliqua. Ut enim ad minim veniam, quis nostrud exercitation ullamco.</p>
  <p class="about-body">Nostrud exercitation ullamco laboris nisi ut aliquip ex ea commodo consequat. Duis aute irure dolor in reprehenderit in voluptate velit esse cillum dolore eu fugiat. Nulla pariatur. Excepteur sint occaecat cupidatat non proident, sunt in culpa qui.</p>
</section>

<footer class="site-footer">
  <div class="foot-head" style="left:164px">Quick Links</div>
  <div class="foot-rule" style="left:164px"></div>
  <ul class="quick-links">
    <li>Integrated Marketing</li><li>Services</li><li>News &amp; Events</li><li>RideKeepers™</li><li>Blog</li><li>Contact Us</li>
  </ul>

  <div class="foot-head" style="left:384px">Contact Form</div>
  <div class="foot-rule" style="left:384px"></div>
  <div class="field" style="top:82px;height:22px">Enter your Email</div>
  <div class="field" style="top:110px;height:22px">Subject</div>
  <div class="field" style="top:138px;height:62px">Your Message</div>
  <div class="submit">Submit</div>

  <div class="foot-head" style="left:638px">Latest News</div>
  <div class="foot-rule" style="left:638px"></div>
  <div class="news" style="top:94px"><div class="news-date"><b>Aug</b><span>15</span></div><p>Lorem tempor incididunt ut labore et dolore magna aliqua. Ut enim ad minim veniam quis nostrud exercitation ullamco [Read More]</p></div>
  <div class="news-rule" style="top:144px"></div>
  <div class="news" style="top:160px"><div class="news-date"><b>Aug</b><span>15</span></div><p>Lorem tempor incididunt ut labore et dolore magna aliqua. Ut enim ad minim veniam quis nostrud exercitation ullamco [Read More]</p></div>
  <div class="news-rule" style="top:208px"></div>
  <div class="view-all">View All</div>

  <div class="foot-head" style="left:886px">Connect with Us</div>
  <div class="foot-rule" style="left:886px"></div>
  <ul class="social">
    <li>Linkfeed<i style="background:#3b5a98"></i></li>
    <li>Chirpline<i style="background:#2ba6de"></i></li>
    <li>Circlespace<i style="background:#d64a37"></i></li>
    <li>Reelcast<i style="background:#d21f1f"></i></li>
  </ul>
</footer>

</body>
</html>
```